California Construction Company Needs Lead-Gen Website with e-Store integration to loomcart account

I'm pretty sure you already have our company background info, but just in case you forgot.. We're a small new company in the landscape construction/development industry. Both residential & commercial. We're company that comes from Humble beginnings but with big admirations' for what the future would bring. Our company's culture is that of compassion, integrity, professionalism and self-worth. We have zero tolerance for negativity and laziness. Services include: Landscape installation, Pavers (which is our bread & butter), also we do non-structural concrete, also sprinkler irrigation systems & retaining walls, and much more. The Final Design should be a 7 page design with the Main menu Buttons being: Home|About|Services|Store|Reviews|Blog|Contact Us. We would like to see Some "Call to Action's" Among other CRM features & Client info retention attributes (i.e Employee Application form integration)

Target Market(s)

Our Ideal clients would be:
1. Homeowners looking for a Reliable & Professional Company to hire to improve their quality of life at home.
2. Someone who's hardworking, positive, intellectual persons' looking to be part of a satisfying, honest & rewarding career with opportunity to grow in the company

Coding

Coded - Design and coding required

Number of Pages Required

5+ page

Font styles to use
Serif
Sans Serif
Decorative

Requirements
Must have
• 'Call to action' Button
'contact us' form
SEO
needs to connected to my dropshipping loomcart account
The site must work seamlessly across all platforms
Dropshipping store capabilities
Needs to be able to take online payments with secure processing
Needs to be able to have clients schedule/ book appointments online & be integrated with my business email account
Nice to have
• Our Mission statement somewhere at the top of the page And its not required that you include the design of the statement, The words are what's important. feel free to design as you see fit.

```html
<!DOCTYPE html>
<html lang="en">
<head>
<meta charset="utf-8">
<title>Stonefield LLC – Landscape, Pavers, Concrete</title>
<link href="https://fonts.googleapis.com/css2?family=Teko:wght@400;500;600&family=Poppins:ital,wght@0,400;0,500;0,600;1,400&display=swap" rel="stylesheet">
<style>
:root{
  --navy:#1f2a44;
  --navy-deep:#16203a;
  --green:#6fae3f;
  --ink:#1f2a44;
  --text:#4a4f5c;
  --paper:#f3f3f1;
  --footer:#1b1c1e;
  --white:#ffffff;
}
*{margin:0;padding:0;box-sizing:border-box}
html,body{width:1200px;height:3854px;overflow:hidden}
body{font-family:"Poppins",sans-serif;color:var(--text);background:var(--white);position:relative}
.heading{font-family:"Teko",sans-serif;font-weight:500;color:var(--ink);line-height:1}
.label{font-family:"Teko",sans-serif;font-size:22px;color:var(--green);display:flex;align-items:center;justify-content:center;gap:12px;line-height:1}
.label::before,.label::after{content:"";width:30px;height:2px;background:var(--green)}
.center{text-align:center}
section{position:absolute;left:0;width:1200px}

/* top bar */
.topbar{top:0;height:30px;background:var(--navy-deep);color:#fff;font-size:9px}
.topbar .hours{position:absolute;left:250px;width:176px;height:30px;background:var(--green);display:flex;align-items:center;justify-content:center}
.topbar .contact{position:absolute;left:440px;height:30px;display:flex;align-items:center;gap:26px}
.topbar .contact span{display:flex;align-items:center;gap:7px}

/* header */
.header{top:30px;height:48px;background:#fff;border-bottom:1px solid #e6e6e6}
.logo{position:absolute;left:252px;top:5px}
.logo .name{display:flex;align-items:center;gap:6px;font-family:"Teko",sans-serif;font-weight:600;font-size:29px;color:var(--ink);line-height:1}
.logo .name i{width:11px;height:11px;background:var(--green);display:block}
.logo .tag{font-family:"Teko",sans-serif;font-weight:500;font-size:12px;color:var(--green);letter-spacing:1px;margin-left:20px;line-height:1}
.badge{position:absolute;top:8px;display:flex;gap:12px;align-items:center}
.badge .dot{width:24px;height:24px;border-radius:50%;border:2px solid var(--ink)}
.badge b{font-family:"Teko",sans-serif;font-weight:400;font-size:19px;color:var(--ink);display:block;line-height:1}
.badge small{font-size:9px;display:block;text-align:right;color:var(--text)}
.nav{top:78px;height:30px;background:#fff;border-bottom:1px solid #e6e6e6}
.nav ul{position:absolute;left:258px;top:0;height:30px;display:flex;align-items:center;gap:15px;list-style:none;font-size:9px;font-weight:600;color:var(--ink)}
.nav .quote{position:absolute;left:821px;top:0;width:126px;height:30px;background:var(--green);color:#fff;font-size:9px;display:flex;align-items:center;justify-content:center;gap:8px}

/* hero */
.hero{top:108px;height:558px;overflow:hidden}
.hero .photo{position:absolute;inset:0;background:
  radial-gradient(ellipse 560px 300px at 860px 250px,#4a4440 0%,rgba(74,68,64,.85) 45%,rgba(74,68,64,0) 100%),
  radial-gradient(ellipse 380px 200px at 120px 420px,#3f4346 0%,rgba(63,67,70,0) 100%),
  linear-gradient(180deg,#9db8d3 0%,#7f98b3 22%,#5d6670 48%,#3b3b39 72%,#2c2d25 88%,#34391f 100%)}
.hero .shade{position:absolute;inset:0;background:linear-gradient(90deg,rgba(20,22,26,.15) 0%,rgba(20,22,26,.35) 45%,rgba(20,22,26,0) 80%)}
.hero .copy{position:absolute;left:361px;top:145px;color:#fff}
.hero .copy p{font-family:"Teko",sans-serif;font-weight:500;font-size:25px;line-height:1}
.hero .copy h1{font-family:"Teko",sans-serif;font-weight:600;font-size:72px;line-height:.86;margin-top:12px;letter-spacing:.5px}
.hero .btn{position:absolute;left:363px;top:398px;width:111px;height:30px;background:var(--green);color:#fff;font-size:9px;display:flex;align-items:center;justify-content:center}

/* welcome */
.welcome{top:666px;height:568px;background:var(--paper)}
.welcome .label{position:absolute;top:34px;width:100%}
.welcome h2{position:absolute;top:66px;width:100%;font-size:35px;font-weight:400;line-height:1.15}
.svc{position:absolute;top:190px;width:254px;height:350px;background:#fff;box-shadow:0 4px 14px rgba(0,0,0,.06)}
.svc .img{height:254px}
.svc .body{margin:24px 0 0 20px;border-left:3px solid var(--green);padding-left:19px}
.svc h3{font-family:"Teko",sans-serif;font-weight:500;font-size:20px;color:var(--ink);line-height:1}
.svc p{font-size:11px;color:var(--ink);margin-top:14px;font-weight:500}
.dots{position:absolute;top:558px;width:100%;display:flex;justify-content:center;gap:10px}
.dots i{width:8px;height:8px;border-radius:50%;background:var(--ink)}
.dots i.on{background:var(--green)}

/* stats */
.stats{top:1234px;height:295px;background:radial-gradient(ellipse at 50% 40%,#26335a 0%,var(--navy) 70%)}
.stats .label{position:absolute;top:52px;width:100%}
.stats h2{position:absolute;top:82px;width:100%;font-size:30px;color:#fff;font-weight:400}
.stat{position:absolute;top:152px;width:200px;text-align:center}
.stat b{display:block;font-family:"Teko",sans-serif;font-weight:400;font-size:44px;color:var(--green);line-height:1}
.stat span{display:block;font-family:"Teko",sans-serif;font-size:21px;color:#fff;margin-top:8px;line-height:1}

/* projects */
.projects{top:1529px;height:872px;overflow:hidden}
.projects .photo{position:absolute;left:0;width:1200px}
.projects .row1{top:0;height:484px;background:
  radial-gradient(ellipse 220px 360px at 90px 300px,#e09a26 0%,rgba(224,154,38,.6) 45%,rgba(224,154,38,0) 100%),
  radial-gradient(ellipse 200px 300px at 1060px 220px,#e3b77a 0%,rgba(227,183,122,.5) 50%,rgba(227,183,122,0) 100%),
  linear-gradient(90deg,#6a4a1a 0%,#2f2f2f 20%,#3a3b3d 50%,#8d99a4 80%,#b8c1c9 100%)}
.projects .row2{top:484px;height:388px;background:
  radial-gradient(ellipse 220px 320px at 90px 180px,#e09a26 0%,rgba(224,154,38,.6) 45%,rgba(224,154,38,0) 100%),
  radial-gradient(ellipse 200px 280px at 1060px 160px,#e3b77a 0%,rgba(227,183,122,.5) 50%,rgba(227,183,122,0) 100%),
  linear-gradient(90deg,#6a4a1a 0%,#3a3936 20%,#6c6a66 50%,#8d99a4 80%,#b8c1c9 100%)}
.projects .label{position:absolute;top:52px;width:100%}
.projects h2{position:absolute;top:80px;width:100%;font-size:31px;color:#fff;font-weight:400}
.proj{position:absolute;width:218px;height:329px;background:#fff}
.proj .img{height:217px}
.proj .body{padding:14px 12px 0}
.proj h3{font-family:"Teko",sans-serif;font-weight:500;font-size:18px;color:var(--ink);line-height:1}
.proj p{font-size:9.5px;line-height:1.55;margin-top:8px;color:var(--text)}
.proj a{display:block;font-size:10px;font-weight:600;color:var(--ink);margin-top:10px}

/* testimonials */
.reviews{top:2401px;height:437px;background:linear-gradient(180deg,#86bdd3 0%,#6fa9c2 100%);overflow:hidden}
.reviews .scene{position:absolute;left:0;top:0;width:760px;height:437px;background:
  radial-gradient(ellipse 110px 80px at 175px 115px,#f2c21a 0%,rgba(242,194,26,.75) 45%,rgba(242,194,26,0) 100%),
  radial-gradient(ellipse 300px 170px at 150px 300px,#6e4a38 0%,rgba(110,74,56,.8) 45%,rgba(110,74,56,0) 100%),
  radial-gradient(ellipse 500px 60px at 300px 410px,rgba(60,70,78,.55) 0%,rgba(60,70,78,0) 100%)}
.reviews .label{position:absolute;top:52px;width:100%}
.reviews h2{position:absolute;top:84px;width:100%;font-size:30px;font-weight:400}
.quote-card{position:absolute;top:154px;width:328px;height:202px;background:#fff;padding:32px 28px 0 40px}
.quote-card .q{position:absolute;left:38px;top:12px;font-family:"Teko",sans-serif;font-size:60px;color:#e2e2e2;line-height:1}
.quote-card p{position:relative;font-size:10px;font-style:italic;line-height:1.55;color:var(--text)}
.quote-card .who{display:flex;align-items:center;gap:10px;margin-top:20px}
.quote-card .avatar{width:62px;height:62px;background:radial-gradient(circle at 50% 35%,#d8b98e 0%,#9aa6b4 60%,#5e6f86 100%)}
.quote-card b{display:block;font-family:"Teko",sans-serif;font-weight:400;font-size:17px;color:var(--ink);line-height:1}
.quote-card small{display:block;font-family:"Teko",sans-serif;font-size:14px;color:var(--green)}
.reviews .dots{top:392px}
.reviews .dots i{background:#fff}
.reviews .dots i.on{background:var(--green)}

/* blog */
.blog{top:2838px;height:543px;background:#fff}
.blog .label{position:absolute;top:50px;width:100%}
.blog h2{position:absolute;top:84px;width:100%;font-size:33px;font-weight:400}
.post{position:absolute;top:151px;width:224px}
.post .img{height:265px;position:relative}
.post .tag{position:absolute;left:6px;bottom:0;width:22px;height:80px;background:var(--green);color:#fff;font-family:"Teko",sans-serif;font-size:12px;letter-spacing:1px;writing-mode:vertical-rl;transform:rotate(180deg);display:flex;align-items:center;justify-content:center}
.post .meta{font-family:"Teko",sans-serif;font-size:15px;color:var(--ink);margin-top:20px;display:flex;gap:8px;align-items:center;line-height:1}
.post .meta em{font-style:normal;color:var(--green)}
.post .meta i{width:14px;height:1px;background:var(--ink);display:block}
.post h3{font-family:"Teko",sans-serif;font-weight:400;font-size:20px;color:var(--ink);line-height:1.05;margin-top:12px}

/* partners */
.partners{top:3381px;height:93px;background:#eef0f2;display:flex;align-items:center;justify-content:center;gap:70px}
.partners i{width:62px;height:34px;border-radius:4px;background:#d6dade;display:block}

/* footer */
.footer{top:3474px;height:380px;background:var(--footer);color:#cfcfcf}
.footer .logo{left:252px;top:36px}
.footer .logo .name{color:#fff}
.footer .about{position:absolute;left:252px;top:118px;width:236px;font-size:9px;line-height:1.5;color:#cfcfcf}
.footer .info{position:absolute;left:252px;top:200px;font-size:9px;list-style:none}
.footer .info li{display:flex;gap:12px;align-items:center;margin-bottom:11px}
.footer .social{position:absolute;left:252px;top:290px;display:flex;gap:5px}
.footer .social i{width:17px;height:17px;background:var(--green);display:block}
.footer h4{position:absolute;font-family:"Teko",sans-serif;font-weight:400;font-size:20px;color:var(--green);line-height:1}
.footer .links{position:absolute;left:550px;top:72px;list-style:none;font-size:9px;color:#ddd}
.footer .links li{margin-bottom:9px}
.footer .feed{position:absolute;left:723px;top:84px;width:213px;height:78px;background:linear-gradient(90deg,#4a5a76 0%,#6b5a4e 55%,#a07a5e 100%)}
.footer .news{position:absolute;left:550px;top:278px;width:397px;height:30px;display:flex}
.footer .news span{flex:1;background:#111;font-size:9px;color:#bbb;display:flex;align-items:center;padding-left:8px}
.footer .news b{width:78px;background:var(--green);color:#fff;font-family:"Teko",sans-serif;font-weight:500;font-size:14px;display:flex;align-items:center;justify-content:center}
.footer .copy{position:absolute;left:0;top:346px;width:1200px;border-top:1px solid #2c2d30;padding:10px 0 0 252px;font-size:8.5px}
.footer .copy em{font-style:normal;color:var(--green)}
</style>
</head>
<body>

<section class="topbar">
  <div class="hours">Monday - Saturday &nbsp;7AM - 4:30PM</div>
  <div class="contact">
    <span><svg width="10" height="10" viewBox="0 0 24 24"><path fill="#fff" d="M6.6 10.8a15 15 0 0 0 6.6 6.6l2.2-2.2c.3-.3.7-.4 1-.2 1.1.4 2.3.6 3.6.6.6 0 1 .4 1 1V20c0 .6-.4 1-1 1A17 17 0 0 1 3 4c0-.6.4-1 1-1h3.5c.6 0 1 .4 1 1 0 1.3.2 2.5.6 3.6.1.3 0 .7-.2 1z"/></svg>+1 555.014.2290</span>
    <span><svg width="11" height="9" viewBox="0 0 24 18"><rect x="1" y="1" width="22" height="16" fill="none" stroke="#fff" stroke-width="2"/><path d="M1 1l11 9 11-9" fill="none" stroke="#fff" stroke-width="2"/></svg>hello@stonefieldyards.com</span>
  </div>
</section>

<section class="header">
  <div class="logo">
    <div class="name"><i></i>STONEFIELD LLC</div>
    <div class="tag">LANDSCAPE | PAVERS | CONCRETE</div>
  </div>
  <div class="badge" style="left:568px"><span class="dot"></span><div><b>The Best Landscape Construction</b><small>Solution Provider</small></div></div>
  <div class="badge" style="left:800px"><span class="dot"></span><div><b>Certified Company</b><small>ISO 9001-2020</small></div></div>
</section>

<section class="nav">
  <ul><li>HOME</li><li>ABOUT</li><li>SERVICES</li><li>STORE</li><li>REVIEWS</li><li>BLOG</li><li>CONTACT US</li></ul>
  <div class="quote">REQUEST A QUOTE <span>&rsaquo;</span></div>
</section>

<section class="hero">
  <div class="photo" role="img" aria-label="Stone-clad two-storey house with landscaped front yard under a blue sky"></div>
  <div class="shade"></div>
  <div class="copy">
    <p>We Have More Than 24 Years Experince</p>
    <h1>Excellence in<br>landscaping<br>services</h1>
  </div>
  <div class="btn">Our Services</div>
</section>

<section class="welcome">
  <div class="label">Welcome to Stonefield LLC</div>
  <h2 class="heading center">Professional Landscape<br>Construction/Development Industry</h2>
  <div class="svc" style="left:204px"><div class="img" role="img" aria-label="Lawn and picnic table in front of a wooden house" style="background:radial-gradient(ellipse 160px 90px at 130px 80px,#8a6a4c 0%,rgba(138,106,76,0) 100%),linear-gradient(180deg,#a9b6bd 0%,#6b5440 35%,#4d5a32 70%,#5f8a2e 100%)"></div><div class="body"><h3>LANDSCAPE</h3><p>Read more...</p></div></div>
  <div class="svc" style="left:473px"><div class="img" role="img" aria-label="Curved paver walkway through a garden" style="background:radial-gradient(ellipse 110px 150px at 140px 200px,#c89a66 0%,rgba(200,154,102,0) 100%),linear-gradient(180deg,#6f8f4a 0%,#7e8c55 40%,#a88a5e 75%,#c29b6c 100%)"></div><div class="body"><h3>PAVERS</h3><p>Read more...</p></div></div>
  <div class="svc" style="left:741px"><div class="img" role="img" aria-label="Concrete being poured over rebar mesh" style="background:radial-gradient(ellipse 120px 100px at 110px 190px,#a7a39c 0%,rgba(167,163,156,0) 100%),linear-gradient(180deg,#c48f55 0%,#b39572 40%,#8e8a84 75%,#6e6b66 100%)"></div><div class="body"><h3>CONCRETE</h3><p>Read more...</p></div></div>
  <div class="dots"><i></i><i></i><i class="on"></i></div>
</section>

<section class="stats">
  <div class="label">All Solutions</div>
  <h2 class="heading center">Get A Solution Residential &amp; Commercial</h2>
  <div class="stat" style="left:261px"><b>35+</b><span>Projects Completed</span></div>
  <div class="stat" style="left:499px"><b>1435+</b><span>Work Employed</span></div>
  <div class="stat" style="left:738px"><b>750+</b><span>Work facilities</span></div>
</section>

<section class="projects">
  <div class="photo row1" role="img" aria-label="Excavator on the left and a smiling construction worker in a hard hat on the right"></div>
  <div class="photo row2" role="img" aria-label="Excavator on the left and a construction worker in a hard hat on the right"></div>
  <div class="label">Our Projects</div>
  <h2 class="heading center">Our Latest Works</h2>
  <div class="proj" style="left:253px;top:154px"><div class="img" role="img" aria-label="Compact track loader beside a dump truck" style="background:radial-gradient(ellipse 90px 70px at 110px 130px,#e6e9ec 0%,rgba(230,233,236,0) 100%),linear-gradient(180deg,#c8d3de 0%,#9aa4ae 50%,#4e5257 100%)"></div><div class="body"><h3>Project 1 - Example</h3><p>High Performance Services For Multiple Insdustries And Technologies!</p><a>Read more...</a></div></div>
  <div class="proj" style="left:491px;top:154px"><div class="img" role="img" aria-label="Worker in safety vest reviewing plans" style="background:radial-gradient(ellipse 80px 90px at 109px 140px,#f08a22 0%,rgba(240,138,34,0) 100%),linear-gradient(180deg,#7d7a72 0%,#a89468 40%,#d36e2c 80%,#b94a22 100%)"></div><div class="body"><h3>Project 2 - Example</h3><p>High Performance Services For Multiple Insdustries And Technologies!</p><a>Read more...</a></div></div>
  <div class="proj" style="left:729px;top:154px"><div class="img" role="img" aria-label="Architectural sketch of a modern house" style="background:radial-gradient(ellipse 80px 60px at 110px 110px,#a08a74 0%,rgba(160,138,116,0) 100%),linear-gradient(180deg,#f6f6f5 0%,#e8e6e2 60%,#cfc8c0 100%)"></div><div class="body"><h3>Project 3 - Example</h3><p>High Performance Services For Multiple Insdustries And Technologies!</p><a>Read more...</a></div></div>
  <div class="proj" style="left:250px;top:491px;height:336px"><div class="img" role="img" aria-label="Shovel digging into gravel next to work boots" style="background:radial-gradient(ellipse 70px 60px at 150px 60px,#b84a4a 0%,rgba(184,74,74,0) 100%),linear-gradient(180deg,#8f9398 0%,#6e6e70 50%,#5a5652 100%)"></div><div class="body"><h3>Project 4 - Example</h3><p>High Performance Services For Multiple Insdustries And Technologies!</p><a>Read more...</a></div></div>
  <div class="proj" style="left:492px;top:491px;height:336px"><div class="img" role="img" aria-label="Gloved hands laying paving stones" style="background:radial-gradient(ellipse 100px 70px at 100px 170px,#c08a84 0%,rgba(192,138,132,0) 100%),linear-gradient(180deg,#a4a29e 0%,#948f8a 50%,#a78a82 100%)"></div><div class="body"><h3>Project 5 - Example</h3><p>High Performance Services For Multiple Insdustries And Technologies!</p><a>Read more...</a></div></div>
  <div class="proj" style="left:734px;top:491px;height:336px"><div class="img" role="img" aria-label="Excavator loading a dump truck" style="background:radial-gradient(ellipse 110px 60px at 100px 150px,#6a6864 0%,rgba(106,104,100,0) 100%),linear-gradient(180deg,#c6d2dd 0%,#a5adb4 45%,#7b776e 100%)"></div><div class="body"><h3>Project 6 - Example</h3><p>High Performance Services For Multiple Insdustries And Technologies!</p><a>Read more...</a></div></div>
</section>

<section class="reviews">
  <div class="scene" role="img" aria-label="Yellow hard hat resting on a stack of bricks"></div>
  <div class="label">What our client say</div>
  <h2 class="heading center">Happy With Customers &amp; Clients</h2>
  <div class="quote-card" style="left:253px"><span class="q">&ldquo;</span><p>This is not just another nail salon! These ladies are super talented! My nails have never looked/felt more amazing!! the environment here is so happy and cheery!</p><div class="who"><div class="avatar" role="img" aria-label="Client portrait"></div><div><b>Dorian Welkes</b><small>Contractor</small></div></div></div>
  <div class="quote-card" style="left:609px"><span class="q">&ldquo;</span><p>This is not just another nail salon! These ladies are super talented! My nails have never looked/felt more amazing!! the environment here is so happy and cheery!</p><div class="who"><div class="avatar" role="img" aria-label="Client portrait"></div><div><b>Dorian Welkes</b><small>Contractor</small></div></div></div>
  <div class="dots"><i class="on"></i><i></i></div>
</section>

<section class="blog">
  <div class="label">Latest Articles Updated Daily</div>
  <h2 class="heading center">We Are Here To Learn You More From Blog</h2>
  <div class="post" style="left:250px"><div class="img" role="img" aria-label="Engineer in hard hat reading blueprints" style="background:radial-gradient(ellipse 90px 120px at 120px 170px,#5e7ca6 0%,rgba(94,124,166,0) 100%),linear-gradient(180deg,#eef0f2 0%,#cdd4dc 50%,#8a9cb6 100%)"><span class="tag">BLOG GIRD</span></div><div class="meta"><em>13 Jun</em><i></i>Be the first to comment!</div><h3>Explain to you why they work and what makes people click them</h3></div>
  <div class="post" style="left:486px"><div class="img" role="img" aria-label="Yellow hard hat on architectural plans" style="background:radial-gradient(ellipse 120px 110px at 20px 90px,#f2d31a 0%,rgba(242,211,26,.6) 50%,rgba(242,211,26,0) 100%),linear-gradient(90deg,#f0d53a 0%,#f1ebc8 50%,#eeeeea 100%)"><span class="tag">BLOG GIRD</span></div><div class="meta"><em>13 Jun</em><i></i>Be the first to comment!</div><h3>Present you with examples of 3 posts from authority websites click</h3></div>
  <div class="post" style="left:723px"><div class="img" role="img" aria-label="Skid steer loader working on a rocky site" style="background:radial-gradient(ellipse 100px 80px at 130px 90px,#e4e2de 0%,rgba(228,226,222,0) 100%),linear-gradient(180deg,#b7b3ab 0%,#86827a 50%,#46433e 100%)"><span class="tag">BLOG GIRD</span></div><div class="meta"><em>13 Jun</em><i></i>Be the first to comment!</div><h3>Technology is important for your business, you use technology makes</h3></div>
</section>

<section class="partners">
  <i></i><i></i><i></i><i></i><i></i><i></i>
</section>

<section class="footer">
  <div class="logo">
    <div class="name"><i></i>STONEFIELD LLC</div>
    <div class="tag">LANDSCAPE | PAVERS | CONCRETE</div>
  </div>
  <p class="about">Stonefield is a full service specialty contractor serving the landscape construction/development industry. Both residential &amp; commercial sectors throughout the United States.</p>
  <ul class="info">
    <li><svg width="9" height="11" viewBox="0 0 24 30"><path fill="#6fae3f" d="M12 0a11 11 0 0 0-11 11c0 8 11 19 11 19s11-11 11-19A11 11 0 0 0 12 0zm0 15a4 4 0 1 1 0-8 4 4 0 0 1 0 8z"/></svg>4410 Meadow Bend Rd, Fairhollow, CA 90000</li>
    <li><svg width="10" height="8" viewBox="0 0 24 18"><rect width="24" height="18" fill="#6fae3f"/><path d="M1 1l11 9 11-9" fill="none" stroke="#1b1c1e" stroke-width="2"/></svg>careers@stonefieldyards.com</li>
    <li><svg width="10" height="10" viewBox="0 0 24 24"><path fill="#6fae3f" d="M6.6 10.8a15 15 0 0 0 6.6 6.6l2.2-2.2c.3-.3.7-.4 1-.2 1.1.4 2.3.6 3.6.6.6 0 1 .4 1 1V20c0 .6-.4 1-1 1A17 17 0 0 1 3 4c0-.6.4-1 1-1h3.5c.6 0 1 .4 1 1 0 1.3.2 2.5.6 3.6.1.3 0 .7-.2 1z"/></svg>+1 555-018-4471</li>
  </ul>
  <div class="social"><i></i><i></i><i></i><i></i><i></i></div>
  <h4 style="left:550px;top:42px">Useful links</h4>
  <ul class="links"><li>Home</li><li>About</li><li>Safety</li><li>Experience</li><li>News</li><li>Careers</li><li>Contact Us</li></ul>
  <h4 style="left:723px;top:42px">Follow Us</h4>
  <div class="feed" role="img" aria-label="Social page preview with cover photos"></div>
  <h4 style="left:550px;top:248px">Newsletter</h4>
  <div class="news"><span>Enter your email</span><b>SUBSCRIBE</b></div>
  <div class="copy">Copyright &copy; 2020 <em>Stonefield LLC</em> - <em>Landscape | Pavers | Concrete</em></div>
</section>

</body>
</html>
```